Custom open/closed sign for our young jewellery and silk shop

We are a new jewellery and silk store in Wellington, New Zealand specialising in products sourced from Suzhou, China.

We're after a design for an open/closed sign for our door. I know it sounds odd, but we want to put a bit of effort into making it special.

We've been thinking about designs relating to round Chinese garden moon gates with doors, to match with our round logo in some way, but are open to other ideas.

Our font is Avenir, so try to work with that if you can.

Have attached our logos on black/white for reference.

Target Market(s)

People gazing at our door - people in a hurry, people who don't know who we are, etc

Industry/Entity Type

Jewelry Store

Other font styles liked:
• Avenir Pro

Colors
fece3e
ffffff
000000

Requirements
Must have
• The words "open" and "closed" on each side, possibly with "We are" or "Sorry we're" or something similar.
• Needs to fit within a 300mm square area, but if it's rectangular, aim for a 300x130mm kind of size.
• Writing should be in Avenir and letter spaced similarly to our logo.
Nice to have
• We like the idea of Chinese moon gate (https://en.pavilorex.org/wiki/Arch_door) to fit with our overall Chinese/oriental theme.
• On a black background is probably preferred, but not essential.
Should not have
• Colours that vastly don't match our black/white/yellow theme.

```html
<!DOCTYPE html>
<html lang="en">
<head>
<meta charset="utf-8">
<title>Pingjiang House – Open / Closed Door Sign</title>
<link rel="stylesheet" href="https://fonts.googleapis.com/css2?family=Nunito+Sans:wght@300;400&display=swap">
<style>
  :root {
    --canvas: #ffffff;
    --sign-light: #ffffff;
    --sign-dark: #4d4d4f;
    --ink: #1c1c1c;
    --paper: #ffffff;
    --brand-gold: #f4b24e;
    --lantern-yellow: #fecf3e;
    --lantern-soft: #ffe58f;
  }
  * { margin: 0; padding: 0; box-sizing: border-box; }
  html, body {
    width: 1200px;
    height: 1000px;
    overflow: hidden;
    background: var(--canvas);
    font-family: "Nunito Sans", "Avenir", sans-serif;
  }
  .canvas { position: relative; width: 1200px; height: 1000px; }

  .sign { position: absolute; }
  .sign--open {
    left: 67px; top: 118px; width: 551px; height: 550px;
    background: var(--sign-light);
    outline: 1px solid #e6e6e6;
  }
  .sign--closed {
    left: 593px; top: 450px; width: 509px; height: 508px;
    background: var(--sign-dark);
  }

  .brand { position: absolute; display: flex; flex-direction: column; align-items: center; }
  .brand__mark {
    width: 26px; height: 26px; border-radius: 50%;
    border: 1px solid var(--brand-gold);
    margin-bottom: 8px;
  }
  .brand__name {
    font-weight: 400;
    text-transform: uppercase;
    text-align: center;
    line-height: 1.35;
  }
  .sign--open .brand { left: 40px; top: 38px; width: 132px; }
  .sign--open .brand__name { color: var(--brand-gold); font-size: 13px; letter-spacing: 0.42em; }
  .sign--closed .brand { left: 22px; top: 14px; width: 126px; }
  .sign--closed .brand__mark { width: 24px; height: 24px; }
  .sign--closed .brand__name { color: var(--paper); font-size: 12px; letter-spacing: 0.42em; }

  .lanterns {
    position: absolute;
    border-radius: 0 0 110px 110px;
    background: radial-gradient(circle at 55% 55%, var(--lantern-yellow) 0%, var(--lantern-soft) 60%, rgba(254, 207, 62, 0) 100%);
  }
  .sign--open .lanterns { left: 308px; top: 0; width: 223px; height: 332px; }
  .sign--closed .lanterns { left: 285px; top: 0; width: 205px; height: 307px; }

  .message { position: absolute; text-transform: uppercase; }
  .message__lead { display: block; font-weight: 400; }
  .message__word { display: block; font-weight: 300; line-height: 1; }
  .sign--open .message { left: 50px; top: 464px; color: var(--ink); }
  .sign--open .message__lead { font-size: 17px; letter-spacing: 0.2em; margin-bottom: 2px; }
  .sign--open .message__word { font-size: 46px; letter-spacing: 0.16em; }
  .sign--closed .message { left: 32px; top: 428px; color: var(--paper); }
  .sign--closed .message__lead { font-size: 13px; letter-spacing: 0.16em; margin-bottom: 2px; }
  .sign--closed .message__word { font-size: 37px; letter-spacing: 0.14em; }
</style>
</head>
<body>
<main class="canvas">
  <section class="sign sign--open" aria-label="Open side of the door sign">
    <div class="brand">
      <span class="brand__mark"></span>
      <span class="brand__name">Pingjiang<br>House</span>
    </div>
    <div class="lanterns" role="img" aria-label="Illustration of three round yellow paper lanterns hanging from cords"></div>
    <h1 class="message">
      <span class="message__lead">We are</span>
      <span class="message__word">Open</span>
    </h1>
  </section>

  <section class="sign sign--closed" aria-label="Closed side of the door sign">
    <div class="brand">
      <span class="brand__mark"></span>
      <span class="brand__name">Pingjiang<br>House</span>
    </div>
    <div class="lanterns" role="img" aria-label="Illustration of three round yellow paper lanterns hanging from cords"></div>
    <h2 class="message">
      <span class="message__lead">Sorry we’re</span>
      <span class="message__word">Closed</span>
    </h2>
  </section>
</main>
</body>
</html>
```